Business Card Design Project

I need a business card designed from scratch. I have an existing logo that I can upload in Illustrator for modification or redesign.

The Company is called Rank Harbor http://rankharbor.com.au and we provide Search Engine Optimization services to Australian businesses. The current logo signifies an increase in visitors, profits etc...

There are no restrictions as to the redesign - colours, style etc are all open to change.

Cards will be full colour and one sided printed at http://www.printlorvex.com.au so check their requirements for file format and sizes etc.

I will expect all original files upon completion of project.

Target Market(s)

Any business with a web site looking to improve their search engine rankings

Industry/Entity Type

Business

Requirements
Must have
• I like modern, sleek designs. Clean, not fussy, uncluttered.

```html
<!DOCTYPE html>
<html lang="en">
<head>
<meta charset="utf-8">
<title>Rank Harbor business card</title>
<link rel="stylesheet" href="https://fonts.googleapis.com/css2?family=PT+Sans:wght@400;700&display=swap">
<style>
  :root {
    --backdrop: #e6e7e9;
    --card: #ffffff;
    --brand-blue: #1b6bb5;
    --deep-blue: #1d4f95;
    --brand-yellow: #f7c21b;
    --card-shadow: rgba(0, 0, 0, 0.18);
  }
  * { margin: 0; padding: 0; box-sizing: border-box; }
  html, body {
    width: 1200px;
    height: 1055px;
    overflow: hidden;
    background: var(--backdrop);
    font-family: "PT Sans", Arial, sans-serif;
  }
  .card {
    position: absolute;
    left: 226px;
    width: 733px;
    height: 381px;
    background: var(--card);
    box-shadow: 0 4px 14px var(--card-shadow);
    overflow: hidden;
  }
  .card--front { top: 67px; }
  .card--back { top: 595px; }

  .brand {
    position: absolute;
    display: flex;
    align-items: center;
    gap: 22px;
  }
  .brand__dot {
    width: 54px;
    height: 54px;
    border-radius: 50%;
    background: var(--brand-yellow);
    flex: none;
  }
  .brand__name {
    color: var(--brand-blue);
    font-weight: 700;
    line-height: 1;
    white-space: nowrap;
  }
  .card--front .brand {
    left: 50%;
    top: 50%;
    transform: translate(-50%, -50%);
  }
  .card--front .brand__name { font-size: 78px; }

  .card--back .brand {
    right: 26px;
    top: 78px;
  }
  .card--back .brand__name { font-size: 66px; }

  .contact-band {
    position: absolute;
    height: 38px;
    background: var(--brand-yellow);
    color: var(--deep-blue);
    font-weight: 700;
    display: flex;
    align-items: center;
    padding-left: 24px;
    white-space: nowrap;
    transform-origin: left center;
  }
  .contact-band--phone {
    left: 22px; top: 150px; width: 270px;
    font-size: 22px; letter-spacing: 1px;
    transform: rotate(-14deg);
  }
  .contact-band--web {
    left: 22px; top: 222px; width: 360px;
    font-size: 18px;
    transform: rotate(-4deg);
  }
  .contact-band--email {
    left: 22px; top: 286px; width: 360px;
    font-size: 17px;
    transform: rotate(-4deg);
  }

  .arrow {
    position: absolute;
    left: 410px;
    top: 318px;
    width: 300px;
    height: 40px;
  }

  .person {
    position: absolute;
    left: 418px;
    top: 208px;
    color: var(--brand-blue);
    font-weight: 700;
  }
  .person__name { font-size: 24px; line-height: 1.3; }
  .person__role { font-size: 19px; line-height: 1.4; margin-left: 2px; }
</style>
</head>
<body>
  <section class="card card--front" aria-label="Card front">
    <div class="brand">
      <span class="brand__dot"></span>
      <span class="brand__name">Rank Harbor</span>
    </div>
  </section>

  <section class="card card--back" aria-label="Card back">
    <div class="brand">
      <span class="brand__name">Rank Harbor</span>
    </div>

    <div class="contact-band contact-band--phone">1300 482915</div>
    <div class="contact-band contact-band--web">www.rankharbor.com.au</div>
    <div class="contact-band contact-band--email">milo@rankharbor.com.au</div>

    <div class="person">
      <p class="person__name">Milo Tanner</p>
      <p class="person__role">Internet Marketing Consultant</p>
    </div>

    <svg class="arrow" viewBox="0 0 300 40" aria-hidden="true">
      <rect x="0" y="12" width="255" height="16" fill="var(--brand-blue)"/>
      <polygon points="250,0 300,20 250,40" fill="var(--brand-blue)"/>
    </svg>
  </section>
</body>
</html>
```